Develop a PowerPoint template based on existing logo for a non-profit international alliance of professionals.
Presentations that will be made with this template will include mostly bullet point text and some tables. SOme images could also be included.

Target Market(s)

Governments, private funders

Industry/Entity Type

Non-Profit

Requirements
Must have
• clean and modern feel
Should not have
• no background in the slide area

```html
<!DOCTYPE html>
<html lang="en">
<head>
<meta charset="utf-8">
<title>Alliance Presentation Template</title>
<link rel="stylesheet" href="https://fonts.googleapis.com/css2?family=Source+Sans+3:wght@400;700&display=swap">
<style>
  :root {
    --red: #e21f26;
    --red-deep: #b3222e;
    --white: #ffffff;
    --footer: #2b2b2d;
    --stage: #e9e7e4;
  }
  * { box-sizing: border-box; margin: 0; padding: 0; }
  html, body { width: 1200px; height: 900px; overflow: hidden; }
  body {
    background: var(--stage);
    font-family: "Source Sans 3", Arial, sans-serif;
    position: relative;
  }
  .slide {
    position: absolute;
    width: 552px;
    height: 391px;
    background: var(--white);
    overflow: hidden;
    box-shadow: 0 2px 6px rgba(0,0,0,.18);
  }
  .slide--cover     { left: 29px;  top: 46px; }
  .slide--content-a { left: 612px; top: 46px; }
  .slide--content-b { left: 29px;  top: 470px; }
  .slide--closing   { left: 612px; top: 470px; }

  .footer-bar {
    position: absolute; left: 0; right: 0; bottom: 0; height: 14px;
    background: linear-gradient(90deg, var(--footer), #5a5a5c 50%, var(--footer));
  }

  .glow {
    position: absolute;
    border-radius: 50%;
    background: radial-gradient(circle, rgba(255,90,95,.75) 0%, rgba(240,60,66,.35) 45%, rgba(226,31,38,0) 70%);
  }

  /* cover */
  .cover-band {
    position: absolute; left: 16px; top: 19px; width: 520px; height: 211px;
    border-radius: 5px; overflow: hidden;
    background: linear-gradient(90deg, var(--red) 0%, var(--red) 45%, var(--red-deep) 100%);
  }
  .cover-band .glow { width: 300px; height: 300px; left: 270px; top: -50px; }
  .cover-title {
    position: absolute; left: 37px; top: 150px;
    color: var(--white); font-weight: 700; font-size: 20px; line-height: 1;
  }
  .cover-subtitle {
    position: absolute; left: 37px; top: 175px;
    color: var(--white); font-weight: 400; font-size: 16px; line-height: 1;
  }

  .brand {
    position: absolute; display: flex; align-items: center; gap: 10px; white-space: nowrap;
  }
  .brand__dot {
    width: 28px; height: 28px; border-radius: 50%; background: var(--red); flex: none;
  }
  .brand__name {
    color: var(--red); font-weight: 700; font-size: 24px; line-height: 1;
  }
  .slide--cover .brand { left: 22px; top: 248px; }

  /* content */
  .title-bar {
    position: absolute; left: 17px; top: 19px; width: 518px; height: 52px;
    border-radius: 5px; overflow: hidden;
    background: linear-gradient(90deg, var(--red) 0%, var(--red) 40%, var(--red-deep) 100%);
  }
  .title-bar .glow { width: 110px; height: 110px; left: 405px; top: -30px; }
  .title-bar__text {
    position: absolute; left: 19px; top: 15px;
    color: var(--white); font-weight: 700; font-size: 19px; line-height: 1; text-transform: uppercase;
  }

  /* closing */
  .closing-top {
    position: absolute; left: 0; top: 0; width: 100%; height: 156px; overflow: hidden;
    background: linear-gradient(90deg, var(--red-deep), var(--red) 60%, var(--red));
  }
  .closing-top .glow { width: 320px; height: 320px; left: 200px; top: -40px; }
  .closing-mid {
    position: absolute; left: 0; top: 156px; width: 100%; height: 103px; background: var(--white);
  }
  .closing-bottom {
    position: absolute; left: 0; top: 259px; width: 100%; height: 118px; overflow: hidden;
    background: linear-gradient(90deg, var(--red-deep), var(--red) 60%, var(--red));
  }
  .closing-mid .brand { left: 50%; top: 50%; transform: translate(-50%, -50%); }
  .closing-thanks {
    position: absolute; left: 0; right: 0; top: 12px; text-align: center;
    color: var(--white); font-weight: 700; font-size: 20px; line-height: 1;
  }
</style>
</head>
<body>

  <section class="slide slide--cover">
    <div class="cover-band">
      <div class="glow" role="img" aria-label="Soft circular dot pattern decoration"></div>
      <h1 class="cover-title">Our Software Delivery Process</h1>
      <p class="cover-subtitle">Agile Development</p>
    </div>
    <div class="brand">
      <span class="brand__dot"></span>
      <span class="brand__name">Meridian Exchange Network</span>
    </div>
  </section>

  <section class="slide slide--content-a">
    <div class="title-bar">
      <div class="glow" role="img" aria-label="Soft circular dot pattern decoration"></div>
      <h2 class="title-bar__text">Your Title Here</h2>
    </div>
    <div class="footer-bar"></div>
  </section>

  <section class="slide slide--content-b">
    <div class="title-bar">
      <div class="glow" role="img" aria-label="Soft circular dot pattern decoration"></div>
      <h2 class="title-bar__text">Your Title Here</h2>
    </div>
    <div class="footer-bar"></div>
  </section>

  <section class="slide slide--closing">
    <div class="closing-top">
      <div class="glow" role="img" aria-label="Soft circular dot pattern decoration"></div>
    </div>
    <div class="closing-mid">
      <div class="brand">
        <span class="brand__dot"></span>
        <span class="brand__name">Meridian Exchange Network</span>
      </div>
    </div>
    <div class="closing-bottom">
      <p class="closing-thanks">Thank You</p>
    </div>
    <div class="footer-bar"></div>
  </section>

</body>
</html>
```